Craft brewery website - 7 Harbors Brewery

Looking for a simple site similar to fennwaldbrew.com or tallridgeales.com with the following features:
- incorporates existing logo (file attached)
- has a consistent look and feel throughout the site that works in harmony with the logo. Please suggest a cool font to use!
- incorporates all or some of the attached images
- has the following tabs/pages: home, our story, brews, blog, contact.
- has some sort of prominent image/design under the top menu bar that can be updated with content - so a placeholder for text. Please use this text on home page: "we brew up our passion for honest ingredients, our curiosity for different cultures, and social and environmental consciousness into characteristic beers." And "Beers with a Twist for the good of the world, for the fun of the party"
- has a scrolling set of images under main section that will list beers. Please create five placeholders for beers: Weizenbock, Copper Lantern, Stout, Saison, Rusty Marlow

Brewery

1 page

• Looking for a simple site similar to fennwaldbrew.com with the following features:
• - incorporates existing logo (file attached)
• - has a consistent look and feel throughout the site that works in harmony with the logo. Please suggest a cool font to use!
• - incorporates all or some of the attached images
• - has the following tabs/pages: home, our story, brews, blog, contact.
• - has some sort of prominent image/design under the top menu bar that can be updated with content - so a placeholder for text. Please use this text on home page: "we brew up our passion for honest ingredients, our curiosity for different cultures, and social and environmental consciousness into characteristic beers." And "Beers with a Twist for the good of the world, for the fun of the party"
• - has a scrolling set of images under main section that will list beers. Please create five placeholders for beers: Weizenbock, Copper Lantern, Stout, Saison, Rusty Marlow

```html
<!DOCTYPE html>
<html lang="en">
<head>
<meta charset="utf-8">
<title>7 Harbors Brewery</title>
<link rel="stylesheet" href="https://fonts.googleapis.com/css2?family=Open+Sans:wght@400;600;700&display=swap">
<style>
:root{
  --white:#ffffff;
  --ink:#141414;
  --navy:#1e2a55;
  --charcoal:#343a3d;
  --divider:#d6d6d6;
  --muted:#6f6f6f;
  --rule:#9a9a9a;
  --red:#e8262e;
  --gold:#b8923c;
  --stone:#9c9896;
  --amber:#c98a1f;
  --amber-deep:#a8631a;
  --foam:#f4f1ea;
}
*{margin:0;padding:0;box-sizing:border-box}
html,body{width:1200px;height:2609px;overflow:hidden;background:var(--white)}
body{position:relative;font-family:"Open Sans",Arial,sans-serif;color:var(--ink)}
.abs{position:absolute}

/* Navigation */
.site-nav{position:absolute;left:0;top:0;width:1200px;height:117px;background:var(--white)}
.nav-link{position:absolute;top:55px;font-size:11px;font-weight:600;letter-spacing:.3px;color:var(--ink);text-transform:uppercase;transform:translateX(-50%)}
.nav-divider{position:absolute;top:46px;width:1px;height:34px;background:var(--divider)}
.brand{position:absolute;left:600px;top:40px;transform:translateX(-50%);display:flex;align-items:center;gap:8px;white-space:nowrap}
.brand-dot{width:22px;height:22px;border-radius:50%;background:var(--navy)}
.brand-name{font-size:16px;font-weight:700;color:var(--navy)}
.search-icon{position:absolute;left:1058px;top:52px}

/* Hero */
.hero{position:absolute;left:0;top:117px;width:1200px;height:558px;
  background:linear-gradient(90deg,var(--gold) 0%,#a89470 30%,var(--stone) 55%,#8f8d8b 100%)}
.hero-photo{position:absolute;left:640px;top:0;width:560px;height:558px;
  background:radial-gradient(ellipse at 55% 45%,#d8cbb0 0%,#8d9a6a 35%,rgba(156,152,150,0) 70%)}
.hero-title{position:absolute;left:90px;top:223px;width:620px;font-size:27px;line-height:35px;font-weight:700;color:var(--white)}
.hero-sub{position:absolute;left:90px;top:386px;font-size:13px;color:var(--white)}
.hero-rule{position:absolute;left:90px;top:433px;width:112px;height:2px;background:var(--white)}
.hero-down{position:absolute;left:578px;top:487px;width:44px;height:44px;border-radius:50%;background:var(--white);display:flex;align-items:center;justify-content:center}

/* Brews carousel */
.brews{position:absolute;left:0;top:675px;width:1200px;height:626px;background:var(--charcoal);overflow:hidden}
.brew-card{position:absolute;top:55px;width:393px;height:435px;background:var(--white)}
.brew-bottle{position:absolute;left:150px;top:67px;width:92px;height:274px;border-radius:30px 30px 10px 10px;
  background:linear-gradient(180deg,#c98a2a 0%,#a8561a 60%,#7e3c12 100%)}
.brew-name{position:absolute;left:0;top:364px;width:100%;text-align:center;font-size:13px;font-weight:600}
.brew-desc{position:absolute;left:0;top:381px;width:100%;text-align:center;font-size:13px;color:#333}
.carousel-next{position:absolute;left:1104px;top:433px;width:96px;height:57px;background:var(--red);display:flex;align-items:center;justify-content:center}
.carousel-dots{position:absolute;left:547px;top:546px;display:flex;gap:12px}
.dot{width:13px;height:13px;border-radius:50%;border:1.5px solid var(--white)}
.dot.is-active{background:var(--white)}

/* Story intro */
.intro-title{position:absolute;left:0;top:1362px;width:1200px;text-align:center;font-size:44px;font-weight:600}
.intro-text{position:absolute;left:325px;top:1440px;width:560px;text-align:center;font-size:13.5px;line-height:17px;color:var(--muted)}
.intro-rule{position:absolute;left:553px;top:1547px;width:94px;height:3px;background:var(--rule)}

/* Gallery */
.gallery-tile{position:absolute;top:1614px;height:398px}
.tile-archer{left:90px;width:510px;background:linear-gradient(135deg,#c4a46e 0%,#b29462 50%,#8e7752 100%)}
.tile-figure{left:609px;width:247px;background:linear-gradient(180deg,#d9d2c4 0%,#c5bba9 60%,#a89a86 100%)}
.tile-mural{left:864px;width:247px;background:linear-gradient(180deg,#d4d1c9 0%,#b9b2a4 60%,#6f7056 100%)}
.tile-caption{position:absolute;left:0;width:100%;text-align:center;color:var(--white)}
.tile-title{top:124px;font-size:28px;font-weight:600}
.tile-text{top:184px;left:95px;width:320px;font-size:13px;line-height:21px}
.tile-rule{position:absolute;left:215px;top:259px;width:80px;height:1px;background:var(--white)}
.gallery-rule{position:absolute;left:0;top:2014px;width:1200px;height:1px;background:var(--divider)}

/* Footer */
.site-footer{position:absolute;left:0;top:2015px;width:1200px;height:594px;
  background:linear-gradient(180deg,var(--white) 0%,var(--foam) 20%,#e8dcc2 27%,var(--amber-deep) 33%,var(--amber) 50%,#d49a30 100%)}
.footer-brand{position:absolute;left:0;top:258px;width:100%;display:flex;justify-content:center;align-items:center;gap:8px}
.footer-brand .brand-dot{background:var(--white);width:18px;height:18px}
.footer-brand .brand-name{color:var(--white);font-size:14px}
.footer-rule{position:absolute;left:572px;top:313px;width:56px;height:1px;background:var(--white)}
.footer-address{position:absolute;left:0;width:100%;text-align:center;font-size:10px;line-height:13px;color:var(--white)}
.footer-social{position:absolute;left:0;top:2478px;width:1200px;display:flex;justify-content:center;gap:38px}
.social-link{width:18px;height:18px;border-radius:50%;background:var(--white)}
.footer-copy{position:absolute;left:0;top:2530px;width:1200px;text-align:center;font-size:10px;color:var(--white)}
.footer-links{position:absolute;left:0;top:2549px;width:1200px;display:flex;justify-content:center;gap:14px;font-size:10px;color:var(--white)}
</style>
</head>
<body>

<header class="site-nav">
  <span class="nav-link" style="left:105px">Home</span>
  <span class="nav-divider" style="left:183px"></span>
  <span class="nav-link" style="left:270px">Our Story</span>
  <span class="nav-divider" style="left:358px"></span>
  <span class="nav-link" style="left:435px">Brews</span>
  <div class="brand"><span class="brand-dot"></span><span class="brand-name">7 Harbors Brewery</span></div>
  <span class="nav-link" style="left:756px">Blog</span>
  <span class="nav-divider" style="left:830px"></span>
  <span class="nav-link" style="left:913px">Contact</span>
  <span class="nav-divider" style="left:997px"></span>
  <svg class="search-icon" width="22" height="22" viewBox="0 0 22 22" aria-label="Search">
    <circle cx="9" cy="9" r="7" fill="none" stroke="#1e2a55" stroke-width="2.5"/>
    <line x1="14" y1="14" x2="20" y2="20" stroke="#1e2a55" stroke-width="2.5" stroke-linecap="round"/>
  </svg>
</header>

<section class="hero">
  <div class="hero-photo" role="img" aria-label="Glass of beer with hops and malt grains on a stone slab"></div>
  <h1 class="hero-title">We brew up our passion for honest ingredients, our curiosity for different cultures, and social and environmental consciousness into characteristic beers.</h1>
  <p class="hero-sub">Beers with a Twist for the good of the world, for the fun of the party</p>
  <span class="hero-rule"></span>
  <span class="hero-down">
    <svg width="18" height="12" viewBox="0 0 18 12"><polyline points="2,3 9,10 16,3" fill="none" stroke="#343a3d" stroke-width="2"/></svg>
  </span>
</section>

<section class="brews">
  <article class="brew-card" style="left:90px">
    <div class="brew-bottle" role="img" aria-label="Bottle of Weizenbock"></div>
    <p class="brew-name">Weizenbock</p>
    <p class="brew-desc">Lorem Ipsum is simply</p>
  </article>
  <article class="brew-card" style="left:501px">
    <div class="brew-bottle" role="img" aria-label="Bottle of Stout"></div>
    <p class="brew-name">Stout</p>
    <p class="brew-desc">Lorem Ipsum is simply</p>
  </article>
  <article class="brew-card" style="left:911px">
    <div class="brew-bottle" role="img" aria-label="Bottle of Copper Lantern"></div>
    <p class="brew-name">Copper Lantern</p>
    <p class="brew-desc">Lorem Ipsum is simply</p>
  </article>
  <span class="carousel-next">
    <svg width="12" height="20" viewBox="0 0 12 20"><polyline points="2,2 10,10 2,18" fill="none" stroke="#fff" stroke-width="2"/></svg>
  </span>
  <div class="carousel-dots">
    <span class="dot is-active"></span><span class="dot"></span><span class="dot"></span><span class="dot"></span><span class="dot"></span>
  </div>
</section>

<section>
  <h2 class="intro-title">Lorem Ipsum</h2>
  <p class="intro-text">Lorem Ipsum is simply dummy text of the printing and typesetting industry. Lorem Ipsum has been the industry's standard dummy text ever since the 1500s, when an unknown printer took a galley of type and scrambled it to make a type specimen book. It has survived not only five centuries, but also the leap into electronic typesetting, remaining essentially unchanged</p>
  <span class="intro-rule"></span>

  <div class="gallery-tile tile-archer" role="img" aria-label="Street mural of an archer drawing a bow">
    <p class="tile-caption tile-title">Lorem Ipsum</p>
    <p class="tile-caption tile-text">Lorem Ipsum has been the industry's standard dummy text ever since the 1500s,</p>
    <span class="tile-rule"></span>
  </div>
  <div class="gallery-tile tile-figure" role="img" aria-label="Street mural of a seated costumed figure"></div>
  <div class="gallery-tile tile-mural" role="img" aria-label="Street mural of a knight with a spear beside a visitor"></div>
  <span class="gallery-rule"></span>
</section>

<footer class="site-footer" role="img" aria-label="Close-up of beer foam over amber beer">
  <div class="footer-brand"><span class="brand-dot"></span><span class="brand-name">7 Harbors Brewery</span></div>
  <span class="footer-rule"></span>
  <p class="footer-address" style="top:344px">400 Lorem Ipsum<br>Lorem Ipsum, CO 80000 USA<br>888-555-0144 / 970-555-0124</p>
  <p class="footer-address" style="top:394px">21 Lorem Ipsum<br>Lorem Ipsum, NC 28000 USA<br>888-555-0152 / 828-555-0190</p>
</footer>
<div class="footer-social">
  <span class="social-link" aria-label="Social link"></span>
  <span class="social-link" aria-label="Social link"></span>
  <span class="social-link" aria-label="Social link"></span>
  <span class="social-link" aria-label="Social link"></span>
</div>
<p class="footer-copy">Copyright © 2017 Craft brewery . All rights reserved.</p>
<nav class="footer-links">
  <span>Privacy Policy</span><span>|</span><span>Terms of Use</span><span>|</span><span>Sales and Refunds</span><span>|</span><span>Legal</span><span>|</span><span>Site Map</span>
</nav>

</body>
</html>
```